Easy one-page Web Design with ready made sketch/template

This project have an already made one page Web Design sketch/template that should be used as a base. It needs professional touch and improvements but should be quite straight forward for you to make.

Webpage: Offers local graphical design services

Attached following documents for you:
- PSD sketch
- JPG sketch
- Word file with project description (read carefully)
- Logo

Target Market(s)

Logo design

Industry/Entity Type

Graphic Design

Number of Pages Required

1 page

Requirements
Must have
• Please refer to attached word document.
Nice to have
Should not have

```html
<!DOCTYPE html>
<html lang="sv">
<head>
<meta charset="utf-8">
<title>Markstudion – Logodesign</title>
<link rel="stylesheet" href="https://fonts.googleapis.com/css2?family=Roboto:wght@400;500;700&family=Oswald:wght@500&display=swap">
<style>
  :root {
    --ink: #ffffff;
    --pill: #d9d9d9;
    --pill-text: #333333;
    --dark-pill: #3a3a3a;
    --pill-edge: #9a9a9a;
    --brand-blue: #2a9fd8;
    --orange: #f08a12;
    --orange-deep: #d9720a;
    --yellow: #f5b335;
    --green: #25a24a;
    --gold: #f3c316;
    --brown: #5a4520;
    --frame: #4a4a4a;
    --base: #8f8f8f;
  }
  * { box-sizing: border-box; margin: 0; padding: 0; }
  html, body { width: 1200px; height: 1000px; overflow: hidden; background: #eeeeee; }
  body { font-family: "Roboto", Arial, sans-serif; color: var(--ink); }
  .page { position: relative; width: 1200px; height: 1000px; overflow: hidden; }

  .hero-photo {
    position: absolute; inset: 0;
    background: linear-gradient(135deg, #8a8f8c 0%, #c9bfae 30%, #e6e1d6 50%, #b98a7a 70%, #4d5a6a 100%);
  }
  .hero-shade { position: absolute; inset: 0; background: linear-gradient(180deg, rgba(0,0,0,.15), rgba(0,0,0,0) 40%); }

  .search {
    position: absolute; top: 26px; right: 60px; width: 300px; height: 40px;
    background: rgba(235,235,235,.85); border-radius: 8px;
    display: flex; align-items: center; justify-content: flex-end; padding-right: 10px;
  }
  .nav { position: absolute; top: 92px; right: 40px; display: flex; gap: 18px; align-items: center; }
  .nav a {
    text-decoration: none; color: var(--pill-text); background: var(--pill);
    border-radius: 8px; padding: 10px 22px; font-size: 17px; font-weight: 500;
    box-shadow: 0 2px 4px rgba(0,0,0,.3);
  }
  .nav a.order { font-size: 20px; font-weight: 700; padding: 12px 22px; }

  .brand { position: absolute; top: 150px; left: 40px; display: flex; align-items: center; gap: 12px; }
  .brand-dot { width: 26px; height: 26px; border-radius: 50%; background: var(--brand-blue); }
  .brand-name { font-size: 40px; font-weight: 700; color: var(--brand-blue); }

  .cta-stack { position: absolute; top: 380px; left: 380px; width: 440px; display: flex; flex-direction: column; align-items: center; gap: 12px; }
  .cta {
    background: var(--dark-pill); border: 4px solid var(--pill-edge); border-radius: 14px;
    color: var(--ink); display: flex; align-items: center; gap: 14px;
    box-shadow: 0 3px 6px rgba(0,0,0,.35);
  }
  .cta.how { padding: 12px 24px; font-size: 24px; }
  .cta.how .q { font-size: 34px; font-weight: 700; margin-left: 20px; }
  .cta.from { padding: 8px 34px; font-size: 20px; }
  .cta.price { padding: 8px 30px; font-size: 22px; }

  .offer-band { position: absolute; left: 0; right: 0; bottom: 0; height: 380px; }
  .base-strip { position: absolute; left: 0; right: 0; bottom: 0; height: 90px; background: var(--base); }

  .panel-guarantee {
    position: absolute; left: 0; bottom: 40px; width: 440px; height: 260px;
    background: var(--yellow); border: 6px solid var(--frame);
    display: flex; align-items: center; justify-content: center;
  }
  .guarantee-badge {
    width: 190px; height: 190px; background: var(--brown); border-radius: 12px;
    display: flex; flex-direction: column; align-items: center; justify-content: center; gap: 10px;
  }
  .guarantee-badge .pct { font-size: 40px; font-weight: 500; }
  .guarantee-badge .label { font-size: 14px; font-weight: 700; letter-spacing: 1px; background: #c9a24a; color: var(--brown); padding: 4px 10px; }

  .panel-order { position: absolute; left: 360px; bottom: 120px; width: 470px; height: 300px; }
  .panel-order svg { position: absolute; inset: 0; }
  .order-content { position: absolute; inset: 0; display: flex; flex-direction: column; align-items: center; padding-top: 40px; gap: 14px; }
  .order-title { font-size: 22px; font-weight: 500; letter-spacing: 1px; }
  .order-price { font-size: 20px; letter-spacing: 1px; }

  .panel-rating {
    position: absolute; right: 0; bottom: 230px; width: 400px; height: 170px;
    background: var(--green); border: 6px solid var(--frame);
  }
  .rating-score {
    position: absolute; left: 28px; top: 14px; width: 64px; height: 130px;
    background: var(--gold); color: #222; transform: skewX(-10deg);
    display: flex; flex-direction: column; align-items: center; justify-content: space-around;
    font-weight: 700; font-size: 17px;
  }
  .rating-stars { position: absolute; left: 110px; top: 16px; background: #333; padding: 4px 12px; color: var(--gold); font-size: 18px; letter-spacing: 3px; }
  .rating-text { position: absolute; left: 112px; top: 64px; font-size: 15px; font-weight: 500; line-height: 2.2; letter-spacing: .5px; }
</style>
</head>
<body>
<main class="page">
  <div class="hero-photo" role="img" aria-label="Photo of a design team working together around a desk with laptops, coffee cups and colored pens"></div>
  <div class="hero-shade"></div>

  <div class="search">
    <svg width="26" height="26" viewBox="0 0 26 26"><circle cx="11" cy="11" r="7" fill="none" stroke="#555" stroke-width="3"/><line x1="16" y1="16" x2="23" y2="23" stroke="#555" stroke-width="3"/></svg>
  </div>

  <nav class="nav">
    <a href="#">Products</a>
    <a href="#">Gallery</a>
    <a href="#">FAQ</a>
    <a href="#">Contact Us</a>
    <a href="#" class="order">ORDER LOGO</a>
  </nav>

  <div class="brand">
    <span class="brand-dot"></span>
    <span class="brand-name">Markstudion</span>
  </div>

  <section class="cta-stack">
    <div class="cta how">
      <svg width="24" height="26" viewBox="0 0 24 26"><polygon points="2,1 23,13 2,25" fill="#3aa6e0"/></svg>
      <span>HOW IT WORKS</span><span class="q">?</span>
    </div>
    <div class="cta from">Start From</div>
    <div class="cta price">$ 1495</div>
  </section>

  <section class="offer-band">
    <div class="base-strip"></div>

    <div class="panel-guarantee">
      <div class="guarantee-badge">
        <span class="pct">100%</span>
        <span class="label">NÖJDGARANTI</span>
      </div>
    </div>

    <div class="panel-rating">
      <div class="rating-score"><span>9.0</span><span>9/10</span><span>200+</span></div>
      <div class="rating-stars">★★★★★</div>
      <div class="rating-text">BETYGSÄTTER UTMÄRKT<br>OMDÖMEN</div>
    </div>

    <div class="panel-order">
      <svg viewBox="0 0 470 300" preserveAspectRatio="none">
        <polygon points="0,0 470,0 450,230 235,300 20,230" fill="var(--frame)"/>
        <polygon points="8,8 462,8 443,222 235,290 27,222" fill="var(--orange)"/>
        <polygon points="150,250 320,250 235,290" fill="var(--orange-deep)"/>
      </svg>
      <div class="order-content">
        <span class="order-title">BESTÄLL LOGOTYP</span>
        <svg width="90" height="90" viewBox="0 0 90 90">
          <circle cx="45" cy="45" r="42" fill="#4a3320"/>
          <rect x="22" y="30" width="46" height="32" rx="3" fill="#fff"/>
          <text x="45" y="53" text-anchor="middle" font-family="Roboto, sans-serif" font-weight="700" font-size="18" fill="#4a3320">24h</text>
        </svg>
        <span class="order-price">FRÅN 1495:-</span>
      </div>
    </div>
  </section>
</main>
</body>
</html>
```